Consumer Credit Attorney Needs Logo for Letterhead & Business cards

I need a basic logo or letterhead design for a new law firm in Mobile, Alabama. The firm is called "Harlow T. Benning, PC." We represent people fighting large corporations in cases involving Fair Credit Reporting, Debt Collection, Mortgage Fraud, Truth in Lending, and Wrongful Foreclosures. I don't want anything with scales of justice or columns or the typical lawyer imagery. I ride a bike to court. I keep most of my office in the cloud. I'm a different type of lawyer, and I want a design that is simple, elegant, and made primarily of blue and white.
Updates

The Job is now Payment Committed.  I look forward to seeing your submissions.  Thanks1

Project Deadline Extended
Reason: I have just recently received some new designs and provided feedback on them. You all deserve some time to consider the feedback. Thanks!

Industry/Entity Type

Business

Requirements
Nice to have
• Clear lines and a small footprint on the letterhead. I like several antique styles- Gilded Age, Rococo, Edwardian, even Art Deco.
Should not have
• The only thing I hate is 1990s clip-art style graphics. No illustrations of money, courthouses, scales, columns, etc. I also hate silly fonts, overly fancy or "handwritten" fonts, and Arial font.

```html
<!DOCTYPE html>
<html lang="en">
<head>
<meta charset="utf-8">
<title>Harlow T. Benning, PC — Stationery</title>
<link rel="stylesheet" href="https://fonts.googleapis.com/css2?family=Montserrat:wght@400;600&display=swap">
<style>
  :root {
    --backdrop: #e8e6e5;
    --paper: #ffffff;
    --firm-blue: #175f80;
    --ink: #3a3a3a;
    --muted: #8a8a8a;
    --on-blue-muted: rgba(255,255,255,0.75);
  }
  * { box-sizing: border-box; margin: 0; padding: 0; }
  html, body { width: 1200px; height: 843px; overflow: hidden; }
  body {
    background: var(--backdrop);
    position: relative;
    font-family: "Montserrat", sans-serif;
    color: var(--ink);
  }

  .firm-name {
    font-family: "Montserrat", sans-serif;
    font-weight: 400;
    color: var(--ink);
    white-space: nowrap;
    display: block;
  }
  .web { font-size: 8px; color: var(--muted); letter-spacing: 0.03em; display: block; }
  .contact { font-size: 8px; line-height: 1.6; color: var(--ink); }
  .contact b { font-weight: 600; color: var(--firm-blue); }
  .footer-rule { height: 2px; background: var(--firm-blue); margin-top: 8px; }

  /* Letterhead */
  .letterhead {
    position: absolute; left: 610px; top: 50px;
    width: 530px; height: 745px;
    background: var(--paper);
    box-shadow: 0 2px 6px rgba(0,0,0,0.12);
  }
  .letterhead .masthead {
    position: absolute; right: 46px; top: 44px; text-align: right;
  }
  .letterhead .masthead .web { margin-bottom: 6px; }
  .letterhead .firm-name { font-size: 19px; }
  .letterhead .footer {
    position: absolute; left: 46px; right: 46px; bottom: 44px;
  }

  /* Business cards */
  .card {
    position: absolute; width: 350px; height: 200px;
    box-shadow: 0 2px 6px rgba(0,0,0,0.12);
  }
  .card-front { left: 60px; top: 150px; background: var(--paper); }
  .card-back  { left: 60px; top: 420px; background: var(--firm-blue); }

  .card .brand { position: absolute; left: 30px; top: 52px; }
  .card .firm-name { font-size: 17px; }

  .card-front .details { position: absolute; left: 30px; right: 30px; bottom: 24px; }
  .card-front .details .web { margin-bottom: 6px; }

  .card-back .brand { top: 86px; }
  .card-back .firm-name { color: var(--paper); }
  .card-back .web {
    position: absolute; left: 30px; bottom: 24px;
    color: var(--on-blue-muted);
  }
</style>
</head>
<body>

  <section class="letterhead" aria-label="Letterhead">
    <header class="masthead">
      <span class="web">www.harlowbenning.com</span>
      <span class="firm-name">Harlow T. Benning, PC.</span>
    </header>
    <footer class="footer">
      <p class="contact">410 Dauphin St. Ste 12, Mobile, AL 36602<br>
        <b>T:</b> 251-555-0147 · <b>F:</b> 251-555-0182 · <b>E:</b> info@harlowbenning.com</p>
      <div class="footer-rule"></div>
    </footer>
  </section>

  <section class="card card-front" aria-label="Business card front">
    <div class="brand">
      <span class="firm-name">Harlow T. Benning, PC.</span>
    </div>
    <div class="details">
      <span class="web">www.harlowbenning.com</span>
      <p class="contact">410 Dauphin St. Ste 12, Mobile, AL 36602<br>
        <b>T:</b> 251-555-0147 · <b>F:</b> 251-555-0182 · <b>E:</b> info@harlowbenning.com</p>
      <div class="footer-rule"></div>
    </div>
  </section>

  <section class="card card-back" aria-label="Business card back">
    <div class="brand">
      <span class="firm-name">Harlow T. Benning, PC.</span>
    </div>
    <span class="web">www.harlowbenning.com</span>
  </section>

</body>
</html>
```